Flyer design for guitar parts website

We are looking for an eye catching flyer design to include within our order packaging to persuade our Kivo and Vendri customers to purchase from our website.

The flyer will be double sided, with one side offering buyers a discount for shopping on our website, and the other side advertising our loyalty points scheme, and the benefits the company it.

We've attached our company logo and our loyalty points logo.

I've also attached a banner design we used recently for our rewards program.

Target Market(s)

Males, aged 20 to 65

Colors
f68e4d
f04a51
886aae
3377b5

Requirements
Must have
• The flyer will be A6 size
• The focus of the front must be on the 20% discount for first order.
• The web address must also be prominent, as must our logo
• There will also be a discount code displayed.
• The back fo the flyer will contain the loyalyt points logo, and information about how the points work, and how they can be redeemed

```html
<!DOCTYPE html>
<html lang="en">
<head>
<meta charset="utf-8">
<title>Resonant Rewards – 20% off your first web order</title>
<link href="https://fonts.googleapis.com/css2?family=Chango&family=Montserrat:ital,wght@0,700;0,800;1,800;1,900&family=Libre+Baskerville&display=swap" rel="stylesheet">
<style>
  :root {
    --paper: #ffffff;
    --ink: #111111;
    --logo-ink: #333333;
    --promo-red: #f04a51;
    --edge-grey: #c4c4c4;
    --photo-highlight: #c2c2c2;
    --photo-light: #a4a4a4;
    --photo-mid: #818181;
    --photo-dark: #5c5c5c;
    --photo-shadow: #3e3e3e;
    --badge-black: #151312;
    --badge-text: #ffffff;
  }
  html, body {
    margin: 0;
    padding: 0;
    overflow: hidden;
    background: var(--paper);
  }
  .flyer {
    position: relative;
    width: 846px;
    height: 1200px;
    overflow: hidden;
    background: var(--paper);
  }
  .brand {
    position: absolute;
    top: 160px;
    left: 0;
    width: 846px;
    margin: 0;
    text-align: center;
    font-family: "Montserrat", sans-serif;
    font-weight: 800;
    font-size: 84px;
    line-height: 1.02;
    letter-spacing: 2px;
    color: var(--logo-ink);
    text-transform: uppercase;
  }
  .guitar-photo {
    position: absolute;
    top: 703px;
    left: 0;
    width: 846px;
    height: 497px;
    background:
      radial-gradient(ellipse 260px 120px at 24% 30%, var(--photo-highlight) 0%, transparent 100%),
      radial-gradient(ellipse 420px 260px at 40% 45%, var(--photo-light) 0%, transparent 100%),
      radial-gradient(ellipse 380px 240px at 15% 95%, var(--photo-shadow) 0%, transparent 100%),
      linear-gradient(150deg, var(--photo-mid) 0%, var(--photo-mid) 45%, var(--photo-dark) 100%);
  }
  .promo-shapes {
    position: absolute;
    top: 0;
    left: 0;
  }
  .discount {
    position: absolute;
    left: 97px;
    top: 438px;
    margin: 0;
    font-family: "Chango", sans-serif;
    font-size: 166px;
    line-height: 1;
    color: var(--ink);
    letter-spacing: -6px;
    transform: scaleX(0.8);
    transform-origin: left top;
  }
  .discount-terms {
    position: absolute;
    left: 92px;
    top: 598px;
    margin: 0;
    font-family: "Montserrat", sans-serif;
    font-weight: 700;
    font-size: 34px;
    line-height: 1;
    letter-spacing: 0.4px;
    color: var(--ink);
    white-space: nowrap;
  }
  .discount-terms em {
    font-weight: 900;
    font-style: italic;
  }
  .rule {
    position: absolute;
    left: 81px;
    top: 639px;
    width: 441px;
    height: 1px;
    background: var(--paper);
  }
  .web-address {
    position: absolute;
    left: 81px;
    top: 648px;
    width: 441px;
    margin: 0;
    text-align: center;
    font-family: "Montserrat", sans-serif;
    font-weight: 900;
    font-style: italic;
    font-size: 20px;
    letter-spacing: 0.5px;
    color: var(--ink);
  }
  .code-badge {
    position: absolute;
    left: 563px;
    top: 423px;
    width: 202px;
    height: 202px;
    display: flex;
    flex-direction: column;
    align-items: center;
    justify-content: center;
    font-family: "Libre Baskerville", serif;
    color: var(--badge-text);
    text-align: center;
  }
  .code-label {
    font-size: 18px;
    letter-spacing: 6px;
    line-height: 1.35;
    padding-left: 6px;
  }
  .code-value {
    font-size: 21px;
    margin-top: 2px;
  }
</style>
</head>
<body>
  <main class="flyer">
    <h1 class="brand">Resonant<br>Rewards</h1>

    <div class="guitar-photo" role="img" aria-label="Black and white close-up photograph of an electric guitar body with pickguard, pickups, strings and toggle switch"></div>

    <svg class="promo-shapes" width="846" height="1200" viewBox="0 0 846 1200" aria-hidden="true">
      <polygon points="0,412 591,412 624,445 704,445 724,412 846,412 846,703 737,703 664,776 591,703 0,703"
               fill="var(--promo-red)" stroke="var(--edge-grey)" stroke-width="1.5"/>
      <circle cx="664" cy="524" r="103" fill="none" stroke="var(--edge-grey)" stroke-width="2"/>
      <circle cx="664" cy="524" r="101" fill="var(--badge-black)"/>
      <circle cx="664" cy="525" r="71" fill="none" stroke="#6a6a6a" stroke-width="0.8"/>
    </svg>

    <p class="discount">20%</p>
    <p class="discount-terms">ON <em>FIRST WEB</em> ORDER</p>
    <div class="rule"></div>
    <p class="web-address">WWW.ADDRESS.COM</p>

    <div class="code-badge">
      <span class="code-label">WITH<br>CODE:</span>
      <span class="code-value">CODE123</span>
    </div>
  </main>
</body>
</html>
```